Honigmüsli Etikett
Zielgruppe
Wir sind eine Imkerei und erzeugen Regionale, Nachhaltige und Biologisch wertvolle Produkte bei denen die umwelt und der umweltschutz sowie die Qualität im vordergrund stehen.
Aufgabenstellung
Der Kunde soll die Natührlichkeit des Produktes im Etikett erkennen.
Es handelt sich hierbei um eine Müslitüte aus braunem Papier mit großem Sichtfenster.
Das Frontetikett sollte nur die wichtigsten und prignanten Dinge aufweisen und das Rückenetikett dann die restlichen Dinge.
Im anhang befindet sich bereits das aktuelle Etikett, welches so im moment auf den Tüten zu sehen ist. Dieses soll nun aber modernisiert und aufgefrischt werden.
Es handelt sich um ein mit Honig gesüßtes Müsli, welches ausschließlich auf gesunde und natührliche Stoffe setzt, dies soll im Etikett wiedergespiegelt werden.
Die Etiketten sind derzeit in den Maßen: 7,5cm x 5cm (Front) und 8,5cm x 6cm (Rücken)
dies ist aber kein muss und kann wenn es möglichkeiten der Etikettgestaltungen gibt die mehr Platz benötigen auch angepasst werden. Das Gesamtbild mit dem großen Fenster sollte allerdings harmonieren und nicht durch ein zu großes Etikett überlagert werden.

```html
<!DOCTYPE html>
<html lang="de">
<head>
<meta charset="utf-8">
<title>Knuspermüsli Etiketten</title>
<link href="https://fonts.googleapis.com/css2?family=Open+Sans:wght@400;700;800&family=Kaushan+Script&family=Oswald:wght@300&display=swap" rel="stylesheet">
<style>
  :root{
    --ink:#231f20;
    --paper:#ffffff;
    --honey-red:#b3121b;
    --wheat-light:#f6efe2;
    --wheat:#e2b765;
    --wheat-deep:#c98f2c;
    --stage:#f4f4f2;
    --muted:#6b6257;
  }
  *{margin:0;padding:0;box-sizing:border-box}
  html,body{width:1151px;height:1200px;overflow:hidden;background:var(--stage)}
  body{position:relative;font-family:"Open Sans",sans-serif;color:var(--ink)}

  .wheat-field{position:absolute;inset:0;
    background:linear-gradient(180deg,var(--wheat-light) 0%,#efd59e 30%,var(--wheat) 62%,var(--wheat-deep) 100%)}

  /* Front label */
  .front-label{position:absolute;left:50px;top:270px;width:486px;height:486px;overflow:hidden;background:var(--paper)}
  .front-label .wheat-field{bottom:58px}
  .brand-box{position:absolute;left:161px;top:0;width:163px;height:146px;background:var(--ink);
    display:flex;flex-direction:column;align-items:center;justify-content:center;gap:10px}
  .brand-dot{width:50px;height:50px;border:2px solid var(--paper);border-radius:50%}
  .brand-name{color:var(--paper);font-weight:700;font-size:16px;letter-spacing:.5px}
  .product-title{position:absolute;left:0;right:0;top:184px;text-align:center;
    font-family:"Kaushan Script",cursive;font-weight:400;font-size:58px;line-height:58px;color:var(--ink)}
  .tagline{position:absolute;left:55px;right:55px;top:318px;display:flex;align-items:center;gap:8px}
  .tagline .rule{flex:1;height:2px;background:var(--ink)}
  .tagline span{color:var(--honey-red);font-weight:800;font-size:17px;letter-spacing:2.5px}
  .own-honey{position:absolute;left:130px;top:346px;color:var(--paper);
    font-family:"Kaushan Script",cursive;font-size:24px;transform:rotate(-6deg)}
  .net-weight{position:absolute;right:46px;top:395px;font-weight:700;font-size:19px}
  .web-band{position:absolute;left:0;right:0;bottom:0;height:58px;background:var(--ink);color:var(--paper);
    display:flex;align-items:center;justify-content:center;font-size:20px;letter-spacing:3px}

  /* Back label */
  .back-label{position:absolute;left:604px;top:270px;width:495px;height:659px;overflow:hidden;background:var(--paper)}
  .back-label .wheat-field{top:148px;bottom:48px;
    background:linear-gradient(180deg,#ffffff 0%,var(--wheat-light) 18%,#ecd197 45%,var(--wheat) 75%,var(--wheat-deep) 100%)}
  .back-header{position:absolute;left:0;right:0;top:0;height:148px;background:var(--ink);
    display:flex;align-items:center;justify-content:center;gap:14px;color:var(--paper)}
  .back-header .brand-dot{width:62px;height:62px}
  .back-header .brand-name{font-size:22px}
  .back-content{position:absolute;left:0;right:0;top:218px;text-align:center}
  .back-title{font-weight:800;font-size:28px;letter-spacing:4px;line-height:34px}
  .back-sub{color:var(--honey-red);font-weight:700;font-size:23px;line-height:28px}
  .ingredients-head{margin-top:16px;font-weight:700;font-size:19px;line-height:26px}
  .ingredients{font-size:20px;line-height:25px;padding:0 46px}
  .best-before{margin-top:35px;font-weight:700;font-size:19px;line-height:26px}
  .best-before .date{font-family:"Oswald",sans-serif;font-weight:300;font-size:15px;color:var(--muted);margin-left:6px}
  .divider{width:280px;height:2px;background:var(--ink);margin:41px auto 14px}
  .maker{font-weight:700;font-size:19px;line-height:25px}
  .address{font-size:19px;line-height:25px}
  .back-label .web-band{height:48px;font-size:19px}
</style>
</head>
<body>

<section class="front-label">
  <div class="wheat-field" role="img" aria-label="Foto eines goldenen Weizenfelds"></div>
  <div class="brand-box">
    <div class="brand-dot"></div>
    <div class="brand-name">Krauter</div>
  </div>
  <h1 class="product-title">Krauters<br>Knuspermüsli</h1>
  <div class="tagline"><i class="rule"></i><span>MIT HONIG VEREDELT</span><i class="rule"></i></div>
  <p class="own-honey">Honig aus eigener Imkerei</p>
  <p class="net-weight">500 g</p>
  <div class="web-band">WWW.BIENENHOFKRAUTER.DE</div>
</section>

<section class="back-label">
  <div class="back-header">
    <div class="brand-dot"></div>
    <div class="brand-name">Imkerei Krauter</div>
  </div>
  <div class="wheat-field" role="img" aria-label="Foto eines goldenen Weizenfelds"></div>
  <div class="back-content">
    <h2 class="back-title">KNUSPERMÜSLI</h2>
    <p class="back-sub">mit Honig veredelt</p>
    <p class="ingredients-head">Zutaten:</p>
    <p class="ingredients">Haferflocken, Honig, Sonnenblumenkerne, Öl, Mandeln, Rosinen, getrocknete Weinbeeren</p>
    <p class="best-before">Mindestens haltbar bis: <span class="date">01.06.2020</span></p>
    <div class="divider"></div>
    <p class="maker">Imkerei Krauter</p>
    <p class="address">Lindenweg 7 · 34999 Wiesenau</p>
    <p class="address">Telefon +49 12 34 - 56 78 90</p>
  </div>
  <div class="web-band">WWW.BIENENHOFKRAUTER.DE</div>
</section>

</body>
</html>
```